Varnel Solutions requires a new business card.

We are an online professional tool store.

Target Market(s)

We target the professional technician.

Industry/Entity Type

Business

Contact Information for Business Card

VarnelSolutions.com.au

sales@varnelsolutions.com

Requirements
Must have
• Needs to look commercial and professional
Should not have
• No Australian Colors, maps or shapes.
• No Shapes of Tools

```html
<!DOCTYPE html>
<html lang="en">
<head>
<meta charset="utf-8">
<title>Varnel Solutions – Business Card</title>
<link rel="stylesheet" href="https://fonts.googleapis.com/css2?family=Open+Sans:wght@400;600;700&display=swap">
<style>
  :root {
    --brand-blue: #2b3d9e;
    --brand-blue-deep: #26368f;
    --brand-cyan: #1c9fd0;
    --hex-blue: #3a63b8;
    --card-white: #ffffff;
    --canvas-bg: #e8e9ed;
    --text-light: #ffffff;
  }
  * { margin: 0; padding: 0; box-sizing: border-box; }
  html, body {
    width: 1200px; height: 1200px; overflow: hidden;
    background: var(--canvas-bg);
    font-family: "Open Sans", Arial, sans-serif;
  }
  .card {
    position: absolute; left: 150px;
    width: 900px; height: 514px;
    overflow: hidden;
    box-shadow: 0 6px 18px rgba(0,0,0,0.18);
  }
  .card-front { top: 60px; background: var(--brand-blue); }
  .card-back { top: 626px; }

  .front-pattern {
    position: absolute; inset: 0;
    background:
      radial-gradient(ellipse at 15% 25%, rgba(58,99,184,0.55), transparent 45%),
      radial-gradient(ellipse at 85% 70%, rgba(58,99,184,0.6), transparent 45%),
      radial-gradient(ellipse at 20% 90%, rgba(58,99,184,0.45), transparent 40%),
      var(--brand-blue);
  }
  .brand {
    position: absolute; display: flex; align-items: center; gap: 14px;
    font-weight: 600; white-space: nowrap;
  }
  .brand-dot { width: 22px; height: 22px; border-radius: 50%; }
  .front-brand {
    left: 50%; top: 50%; transform: translate(-50%, -50%);
    color: var(--text-light); font-size: 46px;
  }
  .front-brand .brand-dot { background: var(--text-light); width: 28px; height: 28px; }

  .back-shapes { position: absolute; inset: 0; }
  .contact {
    position: absolute; left: 58px; top: 72px;
    color: var(--text-light);
  }
  .contact-name { font-size: 27px; font-weight: 700; line-height: 1.15; }
  .contact-title { font-size: 17px; margin-bottom: 24px; }
  .contact-address { font-size: 17px; line-height: 1.35; margin-bottom: 18px; }
  .contact-line {
    display: flex; align-items: center; gap: 10px;
    font-size: 17px; line-height: 1.55;
  }
  .contact-line svg { width: 15px; height: 15px; flex: none; }
  .back-brand {
    left: 575px; top: 262px;
    color: var(--brand-blue); font-size: 33px;
  }
  .back-brand .brand-dot { background: var(--brand-blue); }
</style>
</head>
<body>
  <section class="card card-front">
    <div class="front-pattern" role="img" aria-label="Soft hexagon pattern background in blue tones"></div>
    <div class="brand front-brand"><span class="brand-dot"></span>Varnel Solutions</div>
  </section>

  <section class="card card-back">
    <svg class="back-shapes" viewBox="0 0 900 514" width="900" height="514" aria-hidden="true">
      <rect width="900" height="514" fill="var(--brand-blue)"/>
      <circle cx="850" cy="390" r="480" fill="var(--brand-cyan)"/>
      <circle cx="870" cy="385" r="448" fill="var(--brand-blue)"/>
      <circle cx="880" cy="372" r="428" fill="var(--card-white)"/>
    </svg>

    <div class="contact">
      <div class="contact-name">Daniel Harrow</div>
      <div class="contact-title">General Manager</div>
      <div class="contact-address">42 Kestrel Road, Brightvale<br>P.O. Box 318, 270 Avenue</div>
      <div class="contact-line">
        <svg viewBox="0 0 16 16"><path d="M3 1.5l3 3-1.6 1.6c.9 2 2.5 3.6 4.5 4.5L10.5 9l3 3-1.8 2C6.5 13.6 2.4 9.5 2 4.3z" fill="#fff"/></svg>
        17046128
      </div>
      <div class="contact-line">
        <svg viewBox="0 0 16 16"><rect x="1" y="3" width="14" height="10" fill="#fff"/><path d="M1 3l7 6 7-6" stroke="#2b3d9e" stroke-width="1.4" fill="none"/></svg>
        sales@varnelsolutions.com
      </div>
      <div class="contact-line">
        <svg viewBox="0 0 16 16" fill="none" stroke="#fff" stroke-width="1.3"><circle cx="8" cy="8" r="6.5"/><ellipse cx="8" cy="8" rx="3" ry="6.5"/><path d="M1.5 8h13M2.5 4.8h11M2.5 11.2h11"/></svg>
        VarnelSolutions.com.au
      </div>
    </div>

    <div class="brand back-brand"><span class="brand-dot"></span>Varnel Solutions</div>
  </section>
</body>
</html>
```